Workvine banner ad for roofing company

We need an ad created for a Workvine banner advertising campaign for a UK based roofing company.

The design should have a large photograph on the background (see attached).
The design should have our Ratewell rating (5 stars).
There should be a large text header at the top which reads "Your local roofing experts"

The following services should be listed:
- New roofs
- General roof repairs
- Drone surveys
- Single ply roofing
- Steel cladding
- Asbestos removal

The company logo needs to be visible (attached). Also the company telephone number 020 7946 0321 and website www.brantleyroofing.com

The advert needs to be horizontal/landscape design. For full spec, please see here: https://business.workvine-example.com/marketing-solutions/success/ads-guide/single-image-ads

Size required: 1.91:1 - 1200 x 628 pixels

```html
<!DOCTYPE html>
<html lang="en">
<head>
<meta charset="utf-8">
<title>Brantley Roofing – Your local roofing experts</title>
<link rel="stylesheet" href="https://fonts.googleapis.com/css2?family=Poppins:wght@500;600;700;800&display=swap">
<style>
  :root {
    --navy: #14357a;
    --brand-blue: #1c56a8;
    --panel-blue: rgba(28, 72, 146, 0.8);
    --binding: #2a2f38;
    --white: #ffffff;
    --ink: #1d1d1d;
    --rating: #2fa56f;
    --bar: rgba(255, 255, 255, 0.9);
  }
  * { box-sizing: border-box; margin: 0; padding: 0; }
  html, body { width: 1200px; height: 628px; overflow: hidden; background: #fff; }
  body { font-family: "Poppins", Arial, sans-serif; }

  .ad {
    position: relative;
    width: 1200px;
    height: 628px;
    overflow: hidden;
  }
  .ad__photo {
    position: absolute;
    inset: 0;
    background:
      linear-gradient(180deg, rgba(240,238,234,0.55) 0%, rgba(240,238,234,0.25) 45%, rgba(240,238,234,0.35) 100%),
      radial-gradient(ellipse 180px 420px at 60px 300px, #8fa97a 0%, rgba(143,169,122,0) 100%),
      radial-gradient(ellipse 260px 200px at 330px 140px, #d7b9a0 0%, rgba(215,185,160,0) 100%),
      radial-gradient(ellipse 240px 180px at 640px 110px, #dcb7a4 0%, rgba(220,183,164,0) 100%),
      radial-gradient(ellipse 220px 260px at 1080px 120px, #c9d2cc 0%, rgba(201,210,204,0) 100%),
      radial-gradient(ellipse 200px 300px at 1120px 460px, #8e9aa3 0%, rgba(142,154,163,0) 100%),
      radial-gradient(ellipse 300px 200px at 600px 560px, #a8b29a 0%, rgba(168,178,154,0) 100%),
      linear-gradient(100deg, #a9b996 0%, #cdc2b3 30%, #c7c9bf 55%, #bcc3c2 80%, #a9b3b3 100%);
  }

  .brand {
    position: absolute;
    top: 30px;
    left: 0;
    width: 100%;
    display: flex;
    justify-content: center;
    align-items: center;
    gap: 12px;
  }
  .brand__dot {
    width: 48px; height: 48px;
    border-radius: 50%;
    background: var(--navy);
  }
  .brand__name {
    font-size: 42px;
    font-weight: 700;
    color: var(--brand-blue);
    letter-spacing: -0.5px;
  }

  .headline {
    position: absolute;
    top: 136px;
    left: 0;
    width: 100%;
    text-align: center;
    font-size: 63px;
    font-weight: 800;
    color: var(--navy);
    letter-spacing: 0;
    text-shadow: 3px 3px 0 var(--white);
  }

  .services {
    position: absolute;
    top: 290px;
    left: 133px;
    display: flex;
    gap: 48px;
  }
  .service-card {
    position: relative;
    width: 280px;
    height: 248px;
    background: var(--panel-blue);
    color: var(--white);
    text-align: center;
    font-size: 26px;
    font-weight: 600;
    line-height: 1.65;
    padding-top: 42px;
    border-top: 6px solid var(--binding);
  }
  .service-card__item + .service-card__item { margin-top: 30px; }

  .trust-bar {
    position: absolute;
    left: 0;
    bottom: 0;
    width: 100%;
    height: 54px;
    background: var(--bar);
    display: flex;
    align-items: center;
    padding-left: 32px;
    font-size: 21px;
    color: var(--ink);
    font-weight: 500;
    white-space: nowrap;
  }
  .trust-bar__label { font-weight: 600; font-size: 22px; margin-right: 18px; }
  .rating-badge {
    width: 166px; height: 31px;
    background: var(--rating);
    margin-right: 14px;
  }
  .trust-bar__platform { font-weight: 600; margin-left: 8px; }
  .trust-bar__sep { margin: 0 14px; font-weight: 400; }
  .trust-bar__phone { font-weight: 600; display: flex; align-items: center; gap: 8px; }
  .trust-bar__web { font-weight: 600; }
</style>
</head>
<body>
<main class="ad">
  <div class="ad__photo" role="img" aria-label="Aerial drone photograph of modern apartment blocks and flat commercial roofs beside a road"></div>

  <header class="brand">
    <span class="brand__dot"></span>
    <span class="brand__name">brantleyroofing</span>
  </header>

  <h1 class="headline">Your local roofing experts !</h1>

  <section class="services">
    <article class="service-card">
      <p class="service-card__item">New roofs</p>
      <p class="service-card__item">General<br>roof repairs</p>
    </article>
    <article class="service-card">
      <p class="service-card__item">Drone surveys</p>
      <p class="service-card__item">Single ply<br>roofing</p>
    </article>
    <article class="service-card">
      <p class="service-card__item">Steel cladding</p>
      <p class="service-card__item">Asbestos<br>removal</p>
    </article>
  </section>

  <footer class="trust-bar">
    <span class="trust-bar__label">Excellent</span>
    <span class="rating-badge" role="img" aria-label="Rated 5 out of 5"></span>
    <span>39 reviews on</span>
    <span class="trust-bar__platform">Ratewell</span>
    <span class="trust-bar__sep">|</span>
    <span class="trust-bar__phone">
      <svg width="18" height="18" viewBox="0 0 24 24"><path d="M6.6 10.8a15.1 15.1 0 0 0 6.6 6.6l2.2-2.2c.3-.3.7-.4 1-.2 1.1.4 2.3.6 3.6.6.6 0 1 .4 1 1V20c0 .6-.4 1-1 1A17 17 0 0 1 3 4c0-.6.4-1 1-1h3.5c.6 0 1 .4 1 1 0 1.3.2 2.5.6 3.6.1.3 0 .7-.2 1z" fill="#1d1d1d"/></svg>
      (020) 7946 0321
    </span>
    <span class="trust-bar__sep">|</span>
    <span class="trust-bar__web">www.brantleyroofing.com</span>
  </footer>
</main>
</body>
</html>
```